Poem Handwritten by Veteran while in the jungle of Vietnam

My parents are celebrating their 50th wedding anniversary this year. I wanted to give them a very memorable gift. On my parents 2nd anniversary, my father was stationed in Vietnam. On that night he was in the jungle waiting till morning and wrote a poem to my mother using his pant leg as paper. I would like this poem to typographically designed to be framed and hung on the wall.

I have attached a picture of the poem below. It will need to be 11x14 when printed for framing. It would be great if there was background or artwork to make it more visually interesting, perhaps in a watercolor. My parents have a transitional style. I have attached some possible color schemes as well. Cool greens, blue, neutral grays, with hints of berries or highlights of yellow. These are just a guide, I would be open to your interpretations.

Thank you for your help. This will hopefully be a gift they will truly treasure as much as the poem itself.

Target Market(s)

My parents who are excited to be celebrating their 50th wedding anniversary. It should have a transitional, mature style.

Font styles to use
Serif
Script

Requirements
Must have
• The poem, typographically designed. There can be a mix of fonts, but legibility is critically important.
• Now that some designs have come through I wanted to give some more guidance of what I'm looking for. I want something that feels sophisticated and artistic.
Nice to have
• A background or art work, using the color schemes attached as a guide. I am really liking the designs that have a full color landscape artwork in the background. The fonts should be elegant and formal. I really like the romantic, muted colors. I had trouble finding similar projects online in the style I wanted until I cam across wedding invites. Those seem to be the most applicable. I've added pictures of some so you can get a sense of what I'm looking for. I am really liking the jungle foliage, starry skies or sunrises.
Should not have
• Cartoon caricatures, fonts that are too illegible when printed. I'm not liking anything whimsical. I don't like the very bright colors for this project.

```html
<!DOCTYPE html>
<html lang="en">
<head>
<meta charset="utf-8">
<title>Anniversary Poem Print</title>
<link rel="stylesheet" href="https://fonts.googleapis.com/css2?family=Allura&family=Libre+Franklin:wght@400;800&display=swap">
<style>
  :root {
    --page-bg: #f4f2ee;
    --leaf-deep: #2f6b1f;
    --leaf-mid: #5c9a34;
    --leaf-light: #a9cf6a;
    --sky-pale: #dcebf0;
    --haze-yellow: #eef3c4;
    --ink-slate: #2c3440;
    --ink-dark: #1e261c;
    --ink-white: #ffffff;
  }
  * { margin: 0; padding: 0; box-sizing: border-box; }
  html, body { width: 1200px; height: 1200px; overflow: hidden; background: var(--page-bg); }
  .print {
    position: absolute; left: 169px; top: 20px; width: 862px; height: 1160px;
    overflow: hidden;
    font-family: "Libre Franklin", Arial, sans-serif;
  }
  .print__art {
    position: absolute; inset: 215px 0 0 0;
    background: linear-gradient(180deg, var(--sky-pale) 0%, #e6f0d6 22%, var(--haze-yellow) 38%, var(--leaf-light) 52%, var(--leaf-mid) 68%, #4a8a2c 85%, var(--leaf-deep) 100%);
  }
  .print__header {
    position: absolute; left: 0; top: 0; width: 100%; height: 215px;
    background: radial-gradient(ellipse at 30% 40%, #7fb548 0%, var(--leaf-mid) 40%, var(--leaf-deep) 100%);
  }
  .print__title {
    position: absolute; left: 0; top: 28px; width: 100%;
    text-align: center; font-family: "Allura", cursive; font-size: 78px; line-height: 66px;
    color: var(--ink-white); text-shadow: 2px 3px 2px rgba(0,0,0,0.65);
  }
  .print__heading {
    position: absolute; left: 0; top: 228px; width: 100%;
    text-align: center; font-weight: 800; font-size: 32px; line-height: 47px;
    color: var(--ink-slate); letter-spacing: -0.5px;
  }
  .poem-column {
    position: absolute; width: 380px; text-align: center;
    font-size: 16.5px; line-height: 23.4px;
  }
  .poem-column--left { left: 53px; top: 337px; }
  .poem-column--right { left: 446px; top: 448px; }
  .stanza { margin-bottom: 23.4px; color: var(--ink-dark); }
  .stanza--on-foliage {
    color: var(--ink-white);
    text-shadow: -1px -1px 0 #1a2414, 1px -1px 0 #1a2414, -1px 1px 0 #1a2414, 1px 1px 0 #1a2414;
  }
  .print__note {
    position: absolute; left: 40px; top: 1078px; width: 782px;
    text-align: center; font-family: "Allura", cursive; font-size: 18px; line-height: 23px;
    color: var(--ink-white);
    text-shadow: -1px -1px 0 #1a2414, 1px -1px 0 #1a2414, -1px 1px 0 #1a2414, 1px 1px 0 #1a2414;
  }
</style>
</head>
<body>
  <main class="print">
    <div class="print__art" role="img" aria-label="Soft watercolour landscape of a jungle landing zone with a helicopter and tall green grass"></div>
    <div class="print__header" role="img" aria-label="Dense green jungle foliage with soldiers in the trees"></div>
    <h1 class="print__title">Happy Anniversary<br>Darling.</h1>
    <h2 class="print__heading">20 July 1970, Monday LZ Professional<br>Harold’s Anniversary Poem</h2>

    <section class="poem-column poem-column--left">
      <p class="stanza">Life’s journey began with a challenge,<br>It was heradlded far and near.<br>The road led on forever,<br>Its completion was known to be dear.</p>
      <p class="stanza">From the garden of light it proceeded,<br>To the valley of shadows it led.<br>Thorns and thistles adorned it,<br>Past abyss and crevice it sped.</p>
      <p class="stanza">The brave surged forward with courage,<br>The wise undaunted pressed on.<br>The mighty held high their banner,<br>We all awaited the down.</p>
      <p class="stanza stanza--on-foliage">Thoughthe pitfalls and hazards were many,<br>The pathway was clearly in wiew.<br>Straight and sure it glided,<br>Its course we know to be true.</p>
      <p class="stanza stanza--on-foliage">I knew you, Sweetheart, beforehand,<br>So precious and sweet were you.<br>Our moments of bliss were priceless,<br>Each day brought us joy anwe.</p>
      <p class="stanza stanza--on-foliage">The call to progression beckoned,<br>At last I would have my chance-<br>To clasp you to me forever,<br>And seal out divine fomance.</p>
    </section>

    <section class="poem-column poem-column--right">
      <p class="stanza">I eagerly started the journey,<br>Though with sorrow, I left you behind.<br>With courage and faith I continued,<br>For I knew, that you later I’d find.</p>
      <p class="stanza">I dilligntly searched for you, Darling,<br>The roadway was both bleak and fair.<br>Though the years grew long in number,<br>I did not give up in despair.</p>
      <p class="stanza stanza--on-foliage">At last in the distance I saw you,<br>So beautiful lovely and sweet!<br>Your attention I struggled to capture,<br>Your love I wrested to meet.</p>
      <p class="stanza stanza--on-foliage">What rapture was mine in fulfillment,<br>As now together we stand,<br>To cherish and love each other,<br>While our plans and dreams expand.</p>
      <p class="stanza stanza--on-foliage">I love you, Darling, forever,<br>My life you have made replete.<br>Our eternal mansion backons,<br>Your love has made it compleete.</p>
    </section>

    <p class="print__note">This poem was writen during the dark of night while on guard duty at LZ Professional in Viet Nam. I was at the time a 2nd Lieutenant in the Infantry. The date was July 1970, our second anniversary. The original was penciled onto my fatigue uniform, arranging only the key thoughts words without light to see</p>
  </main>
</body>
</html>
```